Landscape Company in need of logo and business card update. Current logo file is attached.

I need a business card design for a Woman Owned Landscape business in Kansas City. I do Native plant installation and maintenance as well as mowing, chemical applications and residential and commercial landscaping.
My colors are navy, green and white.
I currently have a logo that can be used or you can redesign it.

Target Market(s)

Residential and commercial

Industry/Entity Type

Landscape

Contact Information for Business Card

On back of current card it lists what I do and website:
BMP/Raingarden Maintenance and Installation, Certified Chemical Applicator for Trees, shrubs, and turf; Landscape Design and Installation for residential and commercial.

Logo Text

Copperleaf Landscape Services, LLC

Font styles to use
Other font styles liked:
• See current font on logo examples

Requirements
Must have
• Phone number: 816-402-7719
• Website: www.copperleaflandscape-example.com
• Colors: Navy, Green, white
• Email: copperleaflandscape@mailbox-example.com
• Address: 418 Birchwood Lane, Riverside, MO 64150
• Name of Person: Marcy Dulwick, owner

```html
<!DOCTYPE html>
<html lang="en">
<head>
<meta charset="utf-8">
<title>Copperleaf Landscape Services – Identity &amp; Business Card</title>
<link href="https://fonts.googleapis.com/css2?family=Arimo:wght@400;700&display=swap" rel="stylesheet">
<style>
  :root{
    --charcoal:#353535;
    --white:#ffffff;
    --leaf:#6cb94a;
    --stone:#bdbdbd;
    --slate:#8a8a8a;
    --backdrop:#ebe8e4;
  }
  *{box-sizing:border-box;margin:0;padding:0}
  html,body{width:1098px;height:1200px;overflow:hidden}
  body{position:relative;background:var(--backdrop);font-family:"Arimo",Arial,sans-serif}

  .panel{position:absolute;top:0;width:549px;height:284px;display:flex;align-items:center;justify-content:center}
  .panel--dark{left:0;background:var(--charcoal)}
  .panel--light{left:549px;background:var(--white)}

  .wordmark{display:flex;align-items:center;color:var(--stone)}
  .wordmark__dot{border-radius:50%;background:var(--leaf);flex:none}
  .wordmark__text{display:flex;flex-direction:column;align-items:flex-start}
  .wordmark__name{font-weight:400;line-height:1}
  .wordmark__sub{font-weight:400;text-transform:uppercase;line-height:1}

  .wordmark--large{gap:18px}
  .wordmark--large .wordmark__dot{width:34px;height:34px}
  .wordmark--large .wordmark__name{font-size:66px;letter-spacing:-.01em}
  .wordmark--large .wordmark__sub{font-size:22px;letter-spacing:.98em;margin-top:20px}

  .wordmark--small{gap:10px}
  .wordmark--small .wordmark__dot{width:18px;height:18px}
  .wordmark--small .wordmark__name{font-size:36px}
  .wordmark--small .wordmark__sub{font-size:13px;letter-spacing:1.02em;margin-top:14px}

  .wordmark--medium{gap:12px}
  .wordmark--medium .wordmark__dot{width:24px;height:24px}
  .wordmark--medium .wordmark__name{font-size:46px}
  .wordmark--medium .wordmark__sub{font-size:17px;letter-spacing:1em;margin-top:16px}

  .card{position:absolute;left:243px;width:609px;height:364px;border-radius:20px;overflow:hidden;box-shadow:0 4px 10px rgba(0,0,0,.18)}
  .card--front{top:354px;background:var(--white)}
  .card--back{top:774px;background:var(--charcoal)}

  .contact-name{position:absolute;left:30px;top:80px;font-size:23px;font-weight:700;color:var(--leaf)}
  .contact-role{position:absolute;left:30px;top:108px;font-size:16px;font-weight:700;color:var(--slate)}
  .contact-list{position:absolute;left:30px;top:190px;list-style:none;font-size:15.5px;color:var(--slate)}
  .contact-list li{display:flex;gap:7px;align-items:flex-start;line-height:20px}
  .contact-list li+li{margin-top:6px}
  .contact-list .address{margin-bottom:16px}
  .contact-list svg{flex:none;margin-top:3px}
  .card--front .wordmark{position:absolute;left:340px;top:130px}

  .footer-rule{position:absolute;left:0;right:0;bottom:60px;height:3px;background:var(--stone)}
  .footer-band{position:absolute;left:0;right:0;bottom:0;height:54px;background:var(--leaf)}
  .card-url{position:absolute;right:30px;bottom:18px;font-size:15px;color:var(--white)}

  .card--back .wordmark{position:absolute;left:50%;top:100px;transform:translateX(-50%)}
  .services{position:absolute;left:40px;right:40px;top:226px;text-align:center;font-size:16.2px;line-height:23px;color:var(--leaf)}
  .back-url{position:absolute;left:0;right:0;top:321px;text-align:center;font-size:15.5px;letter-spacing:.07em;color:var(--stone)}
  .back-url .domain{color:var(--leaf)}
</style>
</head>
<body>

<section class="panel panel--dark">
  <div class="wordmark wordmark--large">
    <span class="wordmark__dot"></span>
    <div class="wordmark__text">
      <span class="wordmark__name">copperleaf</span>
      <span class="wordmark__sub">Landscape</span>
    </div>
  </div>
</section>

<section class="panel panel--light">
  <div class="wordmark wordmark--large">
    <span class="wordmark__dot"></span>
    <div class="wordmark__text">
      <span class="wordmark__name">copperleaf</span>
      <span class="wordmark__sub">Landscape</span>
    </div>
  </div>
</section>

<article class="card card--front">
  <h1 class="contact-name">Marcy Dulwick</h1>
  <p class="contact-role">Owner</p>
  <ul class="contact-list">
    <li class="address">
      <svg width="12" height="16" viewBox="0 0 12 16" aria-hidden="true"><path d="M6 0a6 6 0 0 0-6 6c0 4.5 6 10 6 10s6-5.5 6-10a6 6 0 0 0-6-6zm0 8.5A2.5 2.5 0 1 1 6 3.5a2.5 2.5 0 0 1 0 5z" fill="#6cb94a"/></svg>
      <span>418 Birchwood Lane, Riverside,<br>MO 64150</span>
    </li>
    <li>
      <svg width="14" height="14" viewBox="0 0 14 14" aria-hidden="true"><path d="M1 4c0-2 3-3 6-3s6 1 6 3v1h-3V4H4v1H1zM2 7l2-2h6l2 2v6H2z" fill="#6cb94a"/><circle cx="7" cy="9.5" r="1.8" fill="#fff"/></svg>
      <span>816-402-7719</span>
    </li>
    <li>
      <svg width="14" height="14" viewBox="0 0 14 14" aria-hidden="true"><rect x="0" y="3" width="14" height="9" fill="#6cb94a"/><path d="M0 3l7 5 7-5" stroke="#fff" stroke-width="1.2" fill="none"/></svg>
      <span>copperleaflandscape@mailbox-example.com</span>
    </li>
  </ul>
  <div class="wordmark wordmark--small">
    <span class="wordmark__dot"></span>
    <div class="wordmark__text">
      <span class="wordmark__name">copperleaf</span>
      <span class="wordmark__sub">Landscape</span>
    </div>
  </div>
  <div class="footer-rule"></div>
  <div class="footer-band"></div>
  <p class="card-url">www.copperleaflandscape-example.com</p>
</article>

<article class="card card--back">
  <div class="wordmark wordmark--medium">
    <span class="wordmark__dot"></span>
    <div class="wordmark__text">
      <span class="wordmark__name">copperleaf</span>
      <span class="wordmark__sub">Landscape</span>
    </div>
  </div>
  <p class="services">BMP/Raingarden Maintenance and Installation, Certified Chemical Applicator for Trees, shrubs, and turf; Landscape Design and Installation for residential and commercial.</p>
  <p class="back-url">www.<span class="domain">copperleaflandscape-example</span>.com</p>
</article>

</body>
</html>
```